依頼詳細
◆サイトマップ
01.ホーム
02.当院について
03.医院紹介
04.スタッフ紹介
05.初めての方へ
06.銀歯から自然な白い歯へ
07.歯医者にいけなくなった方へ
08.歯の色を全体的に白くしたい方へ
09.口臭が気になる・歯茎に違和感がある
10.歯並びを整えたい方へ
11.歯が失ってしまった方へ
12.虫歯になってしまった方へ
13.お子様の歯を守りたい方へ
14.求人情報
15.よくあるご質問
16.問い合わせ
17.お知らせ(一覧)
18.お知らせ(詳細)
19.ブログ(一覧)
20.ブログ(詳細)

◆TOPに掲載いただきたいもの
・ヘッダー、ロゴ、営業時間、電話番号
・グローバルナビ
・メインイメージ
・お知らせの新着ボックス
・コンセプト
・強み
・各症状ページへ流入する箇所(サイトマップ06~13の内容)
・その他下層ページ移行用バナー(よくあるご質問、問い合わせ、求人情報)
・ブログの新着ボックス
・グーグルマップ
・フッター(ロゴ、院情報、営業時間、サイトマップ)
※仮で作成したもののためレイアウトの並びはお任せ致します。
ただし、配置してあるコンテンツはすべて含まれるようにしてください。
提案で項目を追加頂く等は参考にさせて頂きたいので大変嬉しいです。

◆デザインについて
・希望するイメージ
知的/清潔な/高級感

・希望デザインカラー
茶系
ベースは白やベージュ系

◆参考URL
https://hirotsudentaloffice.example/
スペースのとり方に高級感を感じとても見やすい印象
TOPのコンテンツ量が少ないと感じる
サイトURL
http://203.0.113.47
ページ数
1ページ
希望イメージ
シンプル 複雑
単色 カラフル
暗い 明るい
日常 高級
遊び心 厳粛
未来的 伝統的
女性的 男性的
希望する色
茶系、ベースは白やベージュ系
納品ファイル
• イラストレーター形式 (.ai)
• フォトショップ形式 (.psd)
補足説明
◆素材について
素材として必要なものがある場合には、Pixmora Stock画像をご使用ください。
その際、通常アセットでダウンロード出来る画像のみを使用してください。
Pixmora Stock以外の素材を使用する際には、
必ず無料で提供いただける物のみご使用ください。
※現在、写真の用意がないのですが、撮影後に差し替える予定です。
イメージとしてPixmora Stock画像を使用して作成ください。

◆ロゴ、外観、内観写真について
下記よりダウンロードしてご使用ください。
https://27.fileport-sample.example/0911-a84c27be5190f3d6e4ab07c2f9d8b3e15
PASS:qvrm
もう少し提案が見たいため、延長させて頂きます。
参考サイトを無視した少し奇抜なアイデアも見てみたいです。
■ 選んだ理由

院内で検討の上、決定致しました。
修正等も快諾いただき大変助かりました。

■ 提案者全員のお礼・コメント

皆様たくさんのご提案ありがとうございました。

```html
<!DOCTYPE html>
<html lang="ja">
<head>
<meta charset="utf-8">
<title>桜木デンタルクリニック</title>
<link href="https://fonts.googleapis.com/css2?family=Cormorant+Garamond:wght@300;400&family=Noto+Serif+JP:wght@300;400;500&display=swap" rel="stylesheet">
<style>
:root{
  --backdrop:#3a3a3a;
  --paper:#ffffff;
  --beige:#f1ece3;
  --beige-deep:#e6ddcf;
  --tan:#c9b896;
  --gold:#a8926a;
  --ink:#4f4538;
  --muted:#8c8072;
  --line:#d8cdbb;
}
*{margin:0;padding:0;box-sizing:border-box}
html,body{width:1200px;height:4236px;overflow:hidden;background:var(--backdrop)}
body{font-family:"Noto Serif JP",serif;color:var(--ink)}
.page{position:absolute;left:88px;top:46px;width:1024px;height:4144px;background:var(--paper);overflow:hidden}
.abs{position:absolute}
.num{font-family:"Cormorant Garamond",serif;font-weight:300;color:transparent;-webkit-text-stroke:1px var(--tan);line-height:1}
.num-solid{font-family:"Cormorant Garamond",serif;font-weight:300;color:var(--tan);line-height:1}
.photo{position:absolute}
.more{position:absolute;width:64px;height:20px;border:1px solid var(--line);font-size:9px;letter-spacing:.1em;text-align:center;line-height:18px;color:var(--muted);background:#fff;font-family:"Cormorant Garamond",serif}
.body-text{font-size:12px;line-height:2;color:var(--muted)}
.en{font-family:"Cormorant Garamond",serif;color:var(--gold);letter-spacing:.15em}

/* header */
.site-header{left:0;top:0;width:1024px;height:56px}
.menu-icon{left:24px;top:22px;width:18px}
.menu-icon span{display:block;height:1px;background:var(--ink);margin-bottom:5px}
.brand-name{font-family:"Noto Serif JP",serif;font-weight:400;color:var(--ink);letter-spacing:.2em;white-space:nowrap}
.site-header .brand-name{left:0;width:1024px;top:18px;text-align:center;font-size:16px}
.tel{right:24px;top:18px;font-family:"Cormorant Garamond",serif;font-size:18px;letter-spacing:.1em;color:var(--gold)}
.tel small{font-size:10px;margin-right:6px}

/* hero */
.hero{left:24px;top:56px;width:976px;height:532px;background:linear-gradient(160deg,#f4efe6 0%,#d9cbb3 40%,#a58d6b 75%,#6e5b45 100%)}
.hero-copy{right:60px;top:230px;color:#fff;font-size:22px;line-height:1.9;letter-spacing:.12em;text-align:left}
.info-bar{left:24px;top:608px;width:976px;height:56px;border-top:1px solid var(--line);border-bottom:1px solid var(--line);font-size:11px;color:var(--muted)}
.info-bar .news{left:20px;top:20px}
.info-bar .news b{color:var(--ink);font-weight:400;margin-right:16px}
.info-bar .hours{right:20px;top:10px;line-height:1.8;text-align:right}
.info-bar .more{left:440px;top:18px}

/* concept */
.band-01{left:0;top:700px;width:520px;height:428px;background:var(--beige)}
.title{font-size:17px;letter-spacing:.1em;color:var(--ink)}

/* symptoms */
.band{left:0;width:1024px;background:var(--beige)}
.card-img{position:absolute;width:160px;height:160px}
.card-cap{position:absolute;width:160px;text-align:center;font-size:12px;line-height:1.7}

/* banners */
.banner-band{left:0;top:2468px;width:1024px;height:320px;background:var(--tan)}
.banner{position:absolute;width:200px;height:200px;border:1px solid rgba(255,255,255,.8);color:#fff;text-align:center}
.banner .jp{margin-top:64px;font-size:15px;letter-spacing:.15em}
.banner .en2{font-family:"Cormorant Garamond",serif;font-size:11px;letter-spacing:.2em;opacity:.85;margin-top:6px}
.banner .n{position:absolute;right:12px;bottom:6px;font-family:"Cormorant Garamond",serif;font-size:44px;font-weight:300;color:rgba(255,255,255,.7)}

/* footer */
.footer-info{font-size:11px;line-height:2.1;color:var(--muted)}
.footer-info b{display:inline-block;width:70px;font-weight:400;color:var(--ink)}
</style>
</head>
<body>
<div class="page">

  <header class="abs site-header">
    <div class="abs menu-icon"><span></span><span></span><span></span></div>
    <p class="abs brand-name">SAKURAGI DENTAL</p>
    <div class="abs tel"><small>Tel.</small>012-345-6789</div>
  </header>

  <section>
    <div class="photo hero" role="img" aria-label="明るい大理石調の受付カウンターがある院内の写真"></div>
    <p class="abs hero-copy">あなたの笑顔のために<br>私たちにできること</p>
    <div class="abs info-bar">
      <p class="abs news"><b>お知らせ</b>2024.04.01　診療時間変更のお知らせ</p>
      <span class="more">MORE</span>
      <p class="abs hours">桜木デンタルクリニック　診療時間 9:30-13:00 / 14:30-19:00<br>〒000-0000 架空県みどり市中央1-2-3　休診日 木・日・祝</p>
    </div>
  </section>

  <section class="concept">
    <div class="abs band-01"></div>
    <div class="photo" style="left:144px;top:730px;width:288px;height:380px;background:linear-gradient(180deg,#e9e4dc,#b8a891 60%,#8d7c66)" role="img" aria-label="診療台と観葉植物のある診察室の写真"></div>
    <h2 class="abs title" style="left:560px;top:790px;font-weight:400">健康管理と先回を視野に</h2>
    <div class="abs num" style="left:860px;top:760px;font-size:96px">01</div>
    <p class="abs body-text" style="left:560px;top:846px;width:300px">当院では治療だけでなく予防を大切に考え、患者様一人ひとりの生活に寄り添った健康管理をご提案します。歯の健康から全身の健康を守ります。</p>
    <span class="more" style="left:560px;top:1010px">MORE</span>
  </section>

  <section class="strength">
    <div class="photo" style="left:584px;top:1148px;width:300px;height:380px;background:linear-gradient(180deg,#d9cfbf,#8a7560 55%,#5d4c3c)" role="img" aria-label="木目調の壁と個室の診療スペースの写真"></div>
    <div class="abs" style="left:144px;top:1288px;width:408px;height:280px;background:var(--beige)"></div>
    <div class="abs num-solid" style="left:170px;top:1310px;font-size:80px">02</div>
    <h2 class="abs title" style="left:280px;top:1334px;font-weight:400">個室、健康の鍵</h2>
    <p class="abs en" style="left:280px;top:1362px;font-size:10px">STRENGTH</p>
    <p class="abs body-text" style="left:170px;top:1410px;width:340px">プライバシーに配慮した個室の診療室をご用意。周りを気にせずリラックスして治療を受けていただけます。丁寧な説明を大切にしています。</p>
    <span class="more" style="left:170px;top:1530px">MORE</span>
  </section>

  <section class="symptoms">
    <div class="abs num" style="left:0;width:1024px;text-align:center;top:1630px;font-size:120px">03</div>
    <p class="abs" style="left:0;width:1024px;text-align:center;top:1752px;font-size:15px;letter-spacing:.2em">症状から探す</p>
    <p class="abs en" style="left:0;width:1024px;text-align:center;top:1782px;font-size:10px">SYMPTOMS</p>
    <div class="abs band" style="top:1820px;height:100px"></div>
    <div class="abs band" style="top:2108px;height:44px"></div>

    <div class="card-img" style="left:144px;top:1840px;background:linear-gradient(160deg,#f6f6f4,#dfe3e4)" role="img" aria-label="白い歯の模型の写真"></div>
    <div class="card-img" style="left:344px;top:1840px;background:linear-gradient(160deg,#f3f0ec,#d8d3cc)" role="img" aria-label="歯科医院の器具の写真"></div>
    <div class="card-img" style="left:544px;top:1840px;background:linear-gradient(160deg,#f7eeea,#e8c8c4)" role="img" aria-label="白く輝く歯の写真"></div>
    <div class="card-img" style="left:744px;top:1840px;background:linear-gradient(160deg,#eef5f8,#bfd9e6)" role="img" aria-label="歯ブラシとコップの写真"></div>
    <p class="card-cap" style="left:144px;top:2010px">銀歯から<br>自然な白い歯へ</p>
    <p class="card-cap" style="left:344px;top:2010px">歯医者に<br>いけなくなった方へ</p>
    <p class="card-cap" style="left:544px;top:2010px">歯の色を全体的に<br>白くしたい方へ</p>
    <p class="card-cap" style="left:744px;top:2010px">口臭が気になる・<br>歯茎に違和感がある</p>
    <span class="more" style="left:192px;top:2066px">MORE</span>
    <span class="more" style="left:392px;top:2066px">MORE</span>
    <span class="more" style="left:592px;top:2066px">MORE</span>
    <span class="more" style="left:792px;top:2066px">MORE</span>

    <div class="card-img" style="left:144px;top:2168px;background:linear-gradient(160deg,#f8f1ef,#e9cfc9)" role="img" aria-label="歯並びを整える矯正器具の写真"></div>
    <div class="card-img" style="left:344px;top:2168px;background:linear-gradient(160deg,#f6f4f1,#e4d6c8)" role="img" aria-label="手のひらにのせた歯の模型の写真"></div>
    <div class="card-img" style="left:544px;top:2168px;background:linear-gradient(160deg,#f4f4f4,#d6d8da)" role="img" aria-label="虫歯治療の器具の写真"></div>
    <div class="card-img" style="left:744px;top:2168px;background:linear-gradient(160deg,#f8efe8,#e9c9b3)" role="img" aria-label="子供用の歯ブラシの写真"></div>
    <p class="card-cap" style="left:144px;top:2338px">歯並びを<br>整えたい方へ</p>
    <p class="card-cap" style="left:344px;top:2338px">歯を失って<br>しまった方へ</p>
    <p class="card-cap" style="left:544px;top:2338px">虫歯になって<br>しまった方へ</p>
    <p class="card-cap" style="left:744px;top:2338px">お子様の歯を<br>守りたい方へ</p>
    <span class="more" style="left:192px;top:2394px">MORE</span>
    <span class="more" style="left:392px;top:2394px">MORE</span>
    <span class="more" style="left:592px;top:2394px">MORE</span>
    <span class="more" style="left:792px;top:2394px">MORE</span>
  </section>

  <section class="abs banner-band">
    <div class="banner" style="left:164px;top:52px"><p class="jp">よくある質問</p><p class="en2">FAQ</p><span class="n">04</span></div>
    <div class="banner" style="left:424px;top:82px"><p class="jp">お問い合わせ</p><p class="en2">CONTACT</p><span class="n">05</span></div>
    <div class="banner" style="left:684px;top:112px"><p class="jp">求人情報</p><p class="en2">RECRUIT</p><span class="n">06</span></div>
  </section>

  <section class="blog">
    <div class="abs" style="left:144px;top:2870px;width:736px;height:80px;background:var(--beige)"></div>
    <div class="abs num" style="left:0;width:1024px;text-align:center;top:2812px;font-size:110px">07</div>
    <p class="abs" style="left:180px;top:2898px;font-size:14px;letter-spacing:.15em">ブログ / お知らせ</p>
    <span class="more" style="left:780px;top:2900px">MORE</span>
    <div class="photo" style="left:144px;top:3000px;width:370px;height:290px;background:linear-gradient(135deg,#bfe0f2,#5fa9d8 60%,#3a86bf)" role="img" aria-label="青い背景に歯の模型と歯ブラシの写真"></div>
    <p class="abs" style="left:560px;top:3020px;font-size:15px;letter-spacing:.08em">ブログ記事タイトルテキスト</p>
    <p class="abs en" style="left:560px;top:3048px;font-size:11px">2024.04.01</p>
    <p class="abs body-text" style="left:560px;top:3090px;width:320px">ブログの本文がここに入ります。日々の診療のことや歯の健康に役立つ情報をお届けします。ぜひご覧ください。</p>
  </section>

  <section class="access">
    <div class="abs num-solid" style="left:110px;top:3392px;font-size:96px">08</div>
    <p class="abs" style="left:230px;top:3436px;font-size:16px;letter-spacing:.2em">アクセス</p>
    <div class="abs" style="left:0;top:3490px;width:1000px;height:330px;background:var(--beige)"></div>
    <div class="photo" style="left:144px;top:3516px;width:750px;height:280px;background:linear-gradient(135deg,#eceae4,#dcdfd8 50%,#e6e2d8)" role="img" aria-label="医院周辺の地図"></div>
    <svg class="abs" style="left:510px;top:3620px" width="20" height="28" viewBox="0 0 20 28"><path d="M10 0C4.5 0 0 4.4 0 9.8 0 17 10 28 10 28s10-11 10-18.2C20 4.4 15.5 0 10 0z" fill="#d9453b"/><circle cx="10" cy="10" r="3.5" fill="#fff"/></svg>
  </section>

  <footer>
    <p class="abs brand-name" style="left:144px;top:3876px;font-size:16px">SAKURAGI DENTAL</p>
    <p class="abs" style="left:144px;top:3924px;font-size:15px;letter-spacing:.1em">桜木デンタルクリニック</p>
    <div class="abs footer-info" style="left:144px;top:3956px">
      <p><b>住所</b>〒000-0000 架空県みどり市中央1-2-3</p>
      <p><b>電話番号</b>012-345-6789</p>
      <p><b>診療時間</b>9:30-13:00 / 14:30-19:00</p>
      <p><b>休診日</b>木・日・祝</p>
    </div>
    <div class="photo" style="left:512px;top:3870px;width:380px;height:220px;background:linear-gradient(180deg,#9aa7b5,#5c6470 55%,#3c3a38)" role="img" aria-label="夕暮れの医院外観の写真"></div>
    <p class="abs" style="left:0;width:1024px;text-align:center;top:4118px;font-size:9px;color:var(--muted);font-family:'Cormorant Garamond',serif;letter-spacing:.1em">© SAKURAGI DENTAL CLINIC All Rights Reserved.</p>
  </footer>

</div>
</body>
</html>
```